Corporate Identity for our Company

For this project we need to explain a few things:
We started off in 1933 as a food processing company with main business of Edible oil sold as T Seal. The main colour were red, black and white but those were simple times. The design became immensely popular because of good product and great marketing. Later on We used a lot of yellow as well on the background for our product designs, wall painting etc and also the label. So the colours of our company became RED, YELLOW, BLACK & WHITE. Please check the website for reference http://zenwaygrainworks.com/edible-oils.php
The family business divided into two parts in 1995. We got T seal for items agonised in class 30 of Indian trademark act & our cousins for class 29. We have since only focused on wheat products and are now looking at capitalising our benefits for other products in class 30 which are food items like Besan, Lentils, salt, spices etc. ( for a complete list please visit http://www.quiblex.com/legal-encyclopedia/trademark-class-30-coffee-flour-rice-products.html)
We have also made a website please check : http://vantelhubdock.net/~tseal/
Username : rovelpage
Password : wendrix@Glade72
You can help by redesigning our stationery, letter pads etc. so we can maintain consistency that enables customer recall/ recognition for our company's profile.
I'm attaching pictures of our current stationary (letter pads) and pictures of our products. This will help you get an idea about our company's current design patterns.
Letter pad:
Dimensions/Size: A4
colours: Any
Information to be added:
Admin. office: 7 B/D Stock Shed,
Jammu (J&K)
Ph. no.: 0191-2867403 ; Fax: 0191-2867459
Units:
Sona Kiran Flour Mills
New Sona Kiran Flour Mills
Lane No. 9
TEMBRA Industrial Complex,
Bari Brahmana, Jammu (J&K)
Ph no. 0192-3584076
Email: support@tsealgoods.com
1) Business cards:
Dimensions: L x B (3.5" x 2 ") printable size
Colours: multi colour
Information:
should contain the T seal logo,
Name of the person
company Address (which you have already)
ph no (we will fill that in)
and email. (we will fill that in)
2) Envelopes:
Dimensions:
L x B (14" x 12")
Colour: Multi
information: T seal logo
contact information and address

```html
<!DOCTYPE html>
<html lang="en">
<head>
<meta charset="utf-8">
<title>T Seal — Business Card</title>
<link href="https://fonts.googleapis.com/css2?family=PT+Serif:wght@400;700&display=swap" rel="stylesheet">
<style>
  :root {
    --backdrop: #ece8e2;
    --yellow-light: #fff27a;
    --yellow: #fde13a;
    --yellow-deep: #f9c900;
    --red: #d42a1c;
    --ink: #1d1d1d;
    --white: #ffffff;
    --rule: #d9534a;
  }
  * { box-sizing: border-box; margin: 0; padding: 0; }
  html, body { width: 1200px; height: 1000px; overflow: hidden; }
  body {
    background: var(--backdrop);
    font-family: "PT Serif", Georgia, serif;
    color: var(--ink);
    position: relative;
  }
  .card {
    position: absolute;
    left: 283px;
    width: 634px;
    height: 362px;
    border-radius: 18px;
  }
  .card-front {
    top: 127px;
    background: radial-gradient(ellipse at 50% 45%, var(--yellow-light) 0%, var(--yellow) 55%, var(--yellow-deep) 100%);
  }
  .card-back {
    top: 510px;
    background: var(--white);
    border: 1.5px solid #2a2a2a;
  }
  .brand {
    position: absolute;
    display: flex;
    flex-direction: column;
    align-items: center;
  }
  .brand-dot {
    border-radius: 50%;
    background: var(--red);
  }
  .brand-name {
    color: var(--red);
    font-weight: 700;
  }
  .card-front .brand {
    left: 0; right: 0; top: 60px;
  }
  .card-front .brand-dot { width: 150px; height: 150px; }
  .card-front .brand-name { font-size: 34px; margin-top: 14px; }
  .website {
    position: absolute;
    left: 0; right: 0; top: 320px;
    text-align: center;
    color: var(--red);
    font-size: 19px;
  }
  .holder { position: absolute; left: 24px; top: 18px; }
  .holder-name { font-size: 19px; font-weight: 700; line-height: 24px; }
  .holder-title { font-size: 15.5px; line-height: 22px; }
  .card-back .brand { right: 30px; top: 26px; width: 132px; }
  .card-back .brand-dot { width: 100px; height: 100px; }
  .card-back .brand-name { font-size: 22px; margin-top: 8px; }
  .rule {
    position: absolute;
    left: 24px; right: 24px; top: 183px;
    height: 1px;
    background: var(--rule);
  }
  .contact {
    position: absolute;
    right: 26px; top: 193px;
    text-align: right;
    font-size: 15.5px;
    line-height: 20.5px;
  }
  .contact-block + .contact-block { margin-top: 9px; }
  .contact-label { text-decoration: underline; }
</style>
</head>
<body>
  <section class="card card-front">
    <div class="brand">
      <div class="brand-dot"></div>
      <div class="brand-name">T Seal</div>
    </div>
    <div class="website">www.tsealgoods.com</div>
  </section>

  <section class="card card-back">
    <div class="holder">
      <div class="holder-name">Rohan Mehra</div>
      <div class="holder-title">Managing Director</div>
    </div>
    <div class="brand">
      <div class="brand-dot"></div>
      <div class="brand-name">T Seal</div>
    </div>
    <div class="rule"></div>
    <div class="contact">
      <div class="contact-block">
        <div><span class="contact-label">Admin. Office</span>:</div>
        <div>7 B/D Stock Shed, Jammu (J&amp;K)</div>
        <div>P: 0191-2867403,&nbsp; F: 0191-2867459</div>
      </div>
      <div class="contact-block">
        <div><span class="contact-label">Units</span>:</div>
        <div>Sona Kiran Flour Mills, TEMBRA Industrial Complex</div>
        <div>Lane No. 9, Bari Brahmana, Jammu (J&amp;K)</div>
        <div>P: 0192-3584076,&nbsp; E: support@tsealgoods.com</div>
      </div>
    </div>
  </section>
</body>
</html>
```